Plum Meadow Label

Design a label for new brand called Plum Meadow. The specific product label :
Plum Meadow Cocoa Butter Lotion. You only need to design the front label.
I have included the logo and a bottle jpeg with 2 bottles on it. Please try your best.

Industry/Entity Type

Product

Requirements
Must have
• text on the label other than the logo:
cocoa butter
lotion
8.5oz/250ml

Original Moisturizing Formula
Smoothes Marks
Protect Skin

__________________________________
- ALTERNATIVE TEXT TO ALSO USE:
Smoothes Dry Skin, Blemishes & Stretch Marks
Softens Hands, Face and Body
Vitamin E

```html
<!DOCTYPE html>
<html lang="en">
<head>
<meta charset="utf-8">
<title>Plum Meadow Label</title>
<link href="https://fonts.googleapis.com/css2?family=Anton&family=Archivo+Black&family=Tinos:wght@400&display=swap" rel="stylesheet">
<style>
  :root {
    --page: #ffffff;
    --label-fill: #f6c08a;
    --label-edge: #e6127e;
    --label-inner: #b07a45;
    --cocoa: #a8784a;
    --pink: #ec1b7f;
    --rose: #dc1f6b;
    --plum: #8e2566;
    --gold: #b39a6e;
    --ink: #1a1a1a;
  }
  html, body {
    margin: 0;
    padding: 0;
    width: 1167px;
    height: 1200px;
    overflow: hidden;
    background: var(--page);
  }
  .label-sheet {
    display: block;
    width: 1167px;
    height: 1200px;
  }
  .label-shape { fill: var(--label-fill); stroke: var(--label-edge); stroke-width: 4; }
  .label-rule { fill: none; stroke: var(--label-inner); stroke-width: 1.5; }
  .display { font-family: "Anton", "Impact", sans-serif; text-anchor: middle; }
  .wide { font-family: "Archivo Black", "Arial Black", sans-serif; text-anchor: middle; }
  .size { font-family: "Tinos", "Times New Roman", serif; fill: var(--ink); text-anchor: middle; }
  .c-cocoa { fill: var(--cocoa); }
  .c-pink { fill: var(--pink); }
  .c-rose { fill: var(--rose); }
  .c-plum { fill: var(--plum); }
  .c-gold { fill: var(--gold); }
</style>
</head>
<body>
<svg class="label-sheet" viewBox="0 0 1167 1200" xmlns="http://www.w3.org/2000/svg">

  <!-- Pump bottle label -->
  <g class="label label--pump">
    <path class="label-shape" d="M200 432 L388 432 L470 520 L498 690 L492 1108 L440 1136 L150 1136 L100 1100 L96 690 L122 520 Z"/>
    <path class="label-rule" d="M204 440 L384 440 L462 524 L490 690 L484 1102 L436 1128 L154 1128 L108 1096 L104 690 L130 524 Z"/>

    <text class="display c-cocoa" x="290" y="505" font-size="60" textLength="185" lengthAdjust="spacingAndGlyphs">COCOA</text>
    <text class="display c-cocoa" x="298" y="565" font-size="65" textLength="265" lengthAdjust="spacingAndGlyphs">BUTTER</text>
    <text class="display c-pink brand-name" x="292" y="668" font-size="56" textLength="290" lengthAdjust="spacingAndGlyphs">Plum Meadow</text>
    <text class="display c-pink" x="298" y="830" font-size="147" textLength="345" lengthAdjust="spacingAndGlyphs">LOTION</text>
    <text class="display c-rose" x="293" y="890" font-size="59" textLength="385" lengthAdjust="spacingAndGlyphs">ORIGINALMOISTURIZING</text>
    <text class="display c-rose" x="300" y="970" font-size="82" textLength="345" lengthAdjust="spacingAndGlyphs">FORMULA</text>
    <text class="display c-plum" x="298" y="1035" font-size="65" textLength="330" lengthAdjust="spacingAndGlyphs">SMOOTHSMARKS</text>
    <text class="display" x="294" y="1095" font-size="59" textLength="315" lengthAdjust="spacingAndGlyphs"><tspan class="c-gold">PROTECTS</tspan><tspan class="c-cocoa">SKIN</tspan></text>
    <text class="size" x="290" y="1121" font-size="26">8.5oz/250ml</text>
  </g>

  <!-- Flip-cap bottle label -->
  <g class="label label--flip">
    <path class="label-shape" d="M648 1085 L648 640 C648 480 770 410 874 410 C978 410 1100 480 1100 640 L1100 1085 Q1100 1105 1080 1105 L668 1105 Q648 1105 648 1085 Z"/>
    <path class="label-rule" d="M656 1080 L656 640 C656 488 774 418 874 418 C974 418 1092 488 1092 640 L1092 1080 Q1092 1097 1076 1097 L672 1097 Q656 1097 656 1080 Z"/>

    <text class="display c-cocoa" x="880" y="520" font-size="88" textLength="175" lengthAdjust="spacingAndGlyphs">COCOA</text>
    <text class="display c-cocoa" x="883" y="600" font-size="82" textLength="265" lengthAdjust="spacingAndGlyphs">BUTTER</text>
    <text class="display c-pink brand-name" x="870" y="700" font-size="62" textLength="360" lengthAdjust="spacingAndGlyphs">Plum Meadow</text>
    <text class="display c-pink" x="860" y="890" font-size="200" textLength="395" lengthAdjust="spacingAndGlyphs">LOTION</text>
    <text class="size" x="0" y="0" font-size="26" transform="translate(1080 790) rotate(-90)">8.5oz/250ml</text>
    <text class="display c-pink" x="873" y="945" font-size="59" textLength="430" lengthAdjust="spacingAndGlyphs">SMOOTHS DRY SKIN</text>
    <text class="display c-plum" x="876" y="1005" font-size="59" textLength="420" lengthAdjust="spacingAndGlyphs">SOFTENS HANDS</text>
    <text class="wide c-plum" x="876" y="1037" font-size="40" textLength="410" lengthAdjust="spacingAndGlyphs">FACE &amp; BODY</text>
    <text class="wide c-gold" x="874" y="1085" font-size="52" textLength="390" lengthAdjust="spacingAndGlyphs">VITAMIN E</text>
  </g>
</svg>
</body>
</html>
```